Pemberton Dialworks Business Card Design

Double Sided Business Card Design for a Locksmith company specializing in Safecracking, safe & vault service.

```html
<!DOCTYPE html>
<html lang="en">
<head>
<meta charset="utf-8">
<title>Pemberton Dialworks Business Card</title>
<link href="https://fonts.googleapis.com/css2?family=Archivo:wght@800&family=Roboto:wght@400;500&display=swap" rel="stylesheet">
<style>
  :root {
    --brand-green: #237a31;
    --ink: #1b1b1b;
    --paper: #ffffff;
    --backdrop: #ecebe8;
  }
  * { box-sizing: border-box; margin: 0; padding: 0; }
  html, body { width: 1200px; height: 800px; overflow: hidden; }
  body {
    background: var(--backdrop);
    display: flex;
    align-items: center;
    justify-content: center;
    gap: 40px;
    font-family: "Roboto", Arial, sans-serif;
  }
  .card {
    position: relative;
    width: 540px;
    height: 309px;
    box-shadow: 0 8px 24px rgba(0,0,0,0.12);
  }
  /* Front side */
  .card-front { background: var(--paper); }
  .front-brand {
    position: absolute;
    left: 36px; top: 44px;
    display: flex; align-items: center; gap: 12px;
  }
  .brand-dot {
    width: 46px; height: 46px; border-radius: 50%;
    background: var(--brand-green);
    flex: none;
  }
  .brand-name {
    font-family: "Archivo", Arial, sans-serif;
    font-weight: 800;
    text-transform: uppercase;
    color: var(--brand-green);
    line-height: 1.02;
    letter-spacing: 0.5px;
  }
  .front-brand .brand-name { font-size: 19px; }
  .holder {
    position: absolute;
    right: 38px; top: 48px;
    text-align: right;
  }
  .holder-name {
    font-family: "Archivo", Arial, sans-serif;
    font-weight: 800;
    font-size: 20px;
    color: var(--ink);
    letter-spacing: 0.5px;
  }
  .holder-role {
    font-size: 13px;
    color: var(--brand-green);
    letter-spacing: 1px;
    margin-top: 2px;
  }
  .contact-list {
    position: absolute;
    left: 36px; bottom: 36px;
    list-style: none;
    font-size: 13px;
    color: var(--ink);
  }
  .contact-list li {
    display: flex; align-items: center; gap: 9px;
    margin-top: 5px;
  }
  .contact-list .contact-address { color: var(--brand-green); font-size: 13.5px; }
  .contact-icon { width: 13px; height: 13px; flex: none; }
  .reference {
    position: absolute;
    right: 38px; bottom: 38px;
    font-size: 9px;
    letter-spacing: 1px;
    color: var(--brand-green);
  }
  /* Back side */
  .card-back {
    background: var(--brand-green);
    display: flex; align-items: center; justify-content: center;
  }
  .back-brand { display: flex; align-items: center; gap: 18px; }
  .card-back .brand-dot { width: 82px; height: 82px; background: var(--paper); }
  .card-back .brand-name { color: var(--paper); font-size: 30px; }
  .back-url {
    font-size: 12px;
    color: var(--paper);
    letter-spacing: 1.6px;
    margin-top: 8px;
  }
</style>
</head>
<body>
  <section class="card card-front" aria-label="Business card front">
    <div class="front-brand">
      <span class="brand-dot"></span>
      <div class="brand-name">Pemberton<br>Dialworks</div>
    </div>
    <div class="holder">
      <div class="holder-name">MARCUS HALE</div>
      <div class="holder-role">MANAGER</div>
    </div>
    <ul class="contact-list">
      <li>
        <svg class="contact-icon" viewBox="0 0 16 16"><circle cx="8" cy="8" r="7" fill="none" stroke="#237a31" stroke-width="1.2"/><path d="M5.5 4.5l1.4 1.6-.8 1.1c.5 1.1 1.4 2 2.6 2.6l1.1-.8 1.6 1.4-.9 1.1C7.9 11.4 4.7 8.1 4.5 5.4z" fill="#237a31"/></svg>
        555-014-0182
      </li>
      <li>
        <svg class="contact-icon" viewBox="0 0 16 16"><circle cx="8" cy="8" r="7" fill="none" stroke="#237a31" stroke-width="1.2"/><rect x="4.5" y="5.5" width="7" height="5" rx="0.6" fill="#237a31"/><path d="M4.8 5.9L8 8.3l3.2-2.4" fill="none" stroke="#fff" stroke-width="0.8"/></svg>
        pembertondialworks@mail.com
      </li>
      <li>
        <svg class="contact-icon" viewBox="0 0 16 16"><circle cx="8" cy="8" r="7" fill="none" stroke="#237a31" stroke-width="1.2"/><circle cx="8" cy="8" r="3.6" fill="none" stroke="#237a31" stroke-width="1"/><path d="M4.4 8h7.2M8 4.4c-1.4 2.2-1.4 5 0 7.2M8 4.4c1.4 2.2 1.4 5 0 7.2" fill="none" stroke="#237a31" stroke-width="0.7"/></svg>
        pembertondialworks.com
      </li>
      <li class="contact-address">418 Harrow Lane, Suite 200 Pemberton, OR, 97301</li>
    </ul>
    <div class="reference">L40218653</div>
  </section>

  <section class="card card-back" aria-label="Business card back">
    <div class="back-brand">
      <span class="brand-dot"></span>
      <div>
        <div class="brand-name">Pemberton<br>Dialworks</div>
        <div class="back-url">www.pembertondialworks.com</div>
      </div>
    </div>
  </section>
</body>
</html>
```